E-learning Information & Community Website Needs a Makeover

I'm looking for a design makeover for my website "Vetrola.club". Vetrola's aim is to connect people to online learning through forums, information, guides & independent reviews. The site was launched in September 2014 using a forum software (Xenforo), but now needs a more polished and sophisticated look which communicates expertise and professionalism. I would like to see designs that use the current "Vetrola" blue (#0070c0). To visit the current website, go to http://www.vetrola.club/

Target Market(s)

People wishing to study online

Industry/Entity Type

Club

Number of Pages Required

4 page

Font styles to use
Sans Serif

Requirements
Must have
• A simple, clear and sophisticated lading page with links to the site's key features: discussion forums, Useful resources, Reviews, News etc, Articles. (See layout idea file attached)
• The main pages are the Landing Page, Discussion Forums, Resources & Reviews
• I would like to see designs that use the current "Vetrola" blue (#0070c0).
Nice to have
• Something uncluttered and easy to understand. The design should convey expertise in the field of online learning, giving users a sense of trust in the site's offerings.
• To give an idea of the sort of thing I'm after, take a look at brantivo.com website (screenshot attached)

```html
<!DOCTYPE html>
<html lang="en">
<head>
<meta charset="utf-8">
<title>Vetrola – Connecting People to Online Learning</title>
<link rel="stylesheet" href="https://fonts.googleapis.com/css2?family=Open+Sans:ital,wght@0,300;0,400;0,600;1,400&display=swap">
<style>
:root{
  --brand:#0070c0;
  --link:#1f8fd6;
  --ink:#1a1a1a;
  --muted:#8a8a8a;
  --body:#555;
  --button:#808080;
  --sky:#a8c8eb;
  --sky-strip:#9dbde2;
  --ice:#c6def1;
  --rule:#e2e2e2;
  --white:#fff;
  --tag-article:#e8231f;
  --tag-course:#f4a21a;
  --tag-news:#b8b8b8;
  --tag-event:#7a7a7a;
}
*{box-sizing:border-box;margin:0;padding:0}
html,body{width:960px;height:1200px;overflow:hidden}
body{font-family:"Open Sans",Arial,sans-serif;background:var(--white);color:var(--ink);position:relative}

/* header */
.site-header{position:absolute;left:0;top:0;width:960px;height:52px;background:var(--brand);color:var(--white)}
.brand{position:absolute;left:178px;top:2px}
.brand-name{font-size:23px;font-weight:400;line-height:30px;letter-spacing:.2px}
.brand-tagline{font-size:10.5px;font-weight:600;line-height:14px;margin-top:4px}
.nav-marker{position:absolute;left:417px;top:0}
.main-nav{position:absolute;left:411px;top:15px;display:flex;gap:12px;font-size:9px}
.main-nav a{color:var(--white);text-decoration:none}
.header-tools{position:absolute;left:543px;top:32px;display:flex;align-items:center;gap:4px}
.social-dot{width:14px;height:14px;border-radius:50%;background:#3f8fd3;border:1px solid rgba(255,255,255,.6)}
.subscribe-field{margin-left:4px;width:133px;height:17px;background:var(--white);color:#888;font-size:7px;font-style:italic;line-height:17px;padding-left:5px}
.subscribe-label{font-size:8.5px;font-style:italic;color:#0a1f33;margin-left:2px}

/* hero */
.hero{position:absolute;left:2px;top:52px;width:958px;height:268px;
  background:linear-gradient(100deg,#c9a28c 0%,#e7c9b4 18%,#5d6470 38%,#c37a3a 50%,#ef7b22 58%,#8c6a58 70%,#d8b79f 85%,#bfa896 100%)}
.hero-caption{position:absolute;left:0;bottom:0;width:100%;height:42px;background:rgba(255,255,255,.75);display:flex;align-items:center;padding-left:173px;font-size:13.5px;color:#333}
.hero-caption b{font-weight:600;color:#111}
.hero-caption .cta{color:var(--brand)}
.hero-caption i{font-weight:600}
.hero-dots{position:absolute;right:196px;bottom:14px;display:flex;gap:3px}
.hero-dots span{width:9px;height:9px;border-radius:50%;background:var(--white)}
.hero-dots span.on{background:var(--brand)}

/* features */
.features{position:absolute;left:174px;top:358px;width:612px;display:grid;grid-template-columns:repeat(3,199px);column-gap:7px;align-items:start}
.feature{display:flex;flex-direction:column}
.feature.row1{height:170px}
.feature-title{display:flex;align-items:center;gap:11px;font-size:14px;font-weight:400;color:var(--link);height:28px;border-bottom:2px solid var(--ink)}
.feature-title::before{content:"";border-left:6px solid var(--ink);border-top:4px solid transparent;border-bottom:4px solid transparent;margin-left:2px}
.feature-text{font-size:7.8px;line-height:10.6px;color:var(--body);text-align:justify;margin-top:14px;letter-spacing:-.1px}
.feature-actions{display:flex;justify-content:space-between;margin-top:12px}
.btn{display:inline-block;height:29px;line-height:29px;padding:0 14px;font-size:10px;color:var(--white);background:var(--button);text-decoration:none}
.btn-signup{background:var(--brand);font-style:italic;padding:0 6px}

/* topics */
.topics{position:absolute;left:2px;top:695px;width:958px;height:114px;background:var(--sky)}
.topics-title{text-align:center;font-size:25px;font-weight:300;color:var(--white);margin-top:10px;letter-spacing:.3px}
.topics-strip{position:absolute;left:164px;top:45px;width:650px;height:60px;background:var(--sky-strip);display:flex;align-items:center;justify-content:space-around;padding:0 12px}
.partner{font-size:12px;font-weight:600;color:#1b1b1b}
.partner-mark{width:30px;height:30px;background:#1b1b1b}
.partner-mark.round{border-radius:50%;width:34px;height:34px}

/* community */
.community-title{position:absolute;left:0;top:826px;width:960px;text-align:center;font-size:24px;font-weight:300;color:#111;letter-spacing:.3px}
.threads-head{position:absolute;left:2px;top:867px;width:958px;height:29px;background:var(--ice);font-size:8px;color:#111}
.threads-head span{position:absolute;top:9px}
.threads{position:absolute;left:174px;top:900px;width:600px;list-style:none}
.thread{position:relative;height:44px;border-bottom:1px solid var(--rule)}
.thread:last-child{border-bottom:none}
.avatar{position:absolute;left:3px;top:7px;width:31px;height:31px;border-radius:4px;border:1px solid #bbb}
.avatar.photo{background:linear-gradient(135deg,#8a6a55,#c9a58a)}
.avatar.brand-mark{background:var(--brand);color:var(--white);font-size:6.5px;display:flex;align-items:center;justify-content:center}
.thread-main{position:absolute;left:45px;top:5px;width:310px}
.thread-title{font-size:12.5px;line-height:16px;color:var(--link)}
.tag{display:inline-block;font-size:9px;line-height:12px;padding:0 3px;border-radius:2px;margin-right:2px;color:var(--white);vertical-align:1px}
.tag.article{background:var(--tag-article)}
.tag.course{background:var(--tag-course);color:#222}
.tag.news{background:var(--tag-news);color:#222}
.tag.event{background:var(--tag-event)}
.thread-meta{font-size:8.5px;color:var(--muted);line-height:12px}
.thread-stats{position:absolute;left:365px;top:6px;width:102px;height:34px;border-left:1px solid var(--rule);padding-left:8px;font-size:9.5px;color:var(--muted)}
.stat{display:flex;justify-content:space-between;line-height:14px}
.stat + .stat{font-size:8px;line-height:12px}
.stat b{font-weight:400;color:#222}
.last-post{position:absolute;right:0;top:7px;text-align:right}
.last-post .who{font-size:12.5px;color:var(--link);line-height:15px}
.last-post .when{font-size:8px;color:var(--muted)}
.thread.tall .thread-stats,.thread.tall .last-post{top:12px}
.thread.tall{height:52px}

/* footer */
.site-footer{position:absolute;left:2px;top:1142px;width:958px;height:58px;background:var(--brand)}
.footer-nav{position:absolute;left:172px;top:27px;display:flex;gap:9px;font-size:8.5px}
.footer-nav a{color:#0a1f33;text-decoration:none}
.footer-social{position:absolute;left:721px;top:22px;display:flex;gap:4px}
</style>
</head>
<body>

<header class="site-header">
  <div class="brand">
    <div class="brand-name">Vetrola</div>
    <div class="brand-tagline">Connecting People to Online Learning</div>
  </div>
  <svg class="nav-marker" width="10" height="6" viewBox="0 0 10 6" aria-hidden="true"><path d="M0 0H10L5 6Z" fill="#fff"/></svg>
  <nav class="main-nav">
    <a href="#">Home</a><a href="#">Forums</a><a href="#">Resources</a><a href="#">Members</a><a href="#">FAQ</a><a href="#">Blog</a><a href="#">Vetrola Español</a><a href="#">Learn Scoop</a><a href="#">Login</a>
  </nav>
  <div class="header-tools">
    <span class="social-dot"></span><span class="social-dot"></span><span class="social-dot"></span><span class="social-dot"></span>
    <span class="subscribe-field">Subscribe for Monthly Newsletter</span>
    <span class="subscribe-label">Subscribe</span>
  </div>
</header>

<section class="hero" role="img" aria-label="Photo of smiling students chatting around laptops in a study room">
  <div class="hero-caption">At the heart of&nbsp;<b>connecting people</b>&nbsp;to&nbsp;<b>online</b>&nbsp;learning&nbsp;<span class="cta">Sign Up</span>. Its&nbsp;<i>Free</i></div>
  <div class="hero-dots"><span class="on"></span><span></span><span></span><span></span><span></span></div>
</section>

<section class="features">
  <article class="feature row1">
    <h3 class="feature-title">Getting Started</h3>
    <p class="feature-text">Vetrola.club is a Forum and Community Website for Consumers and Providers of MOOCs and Online Learning to meet, share, debate and learn. The site aims to provide its users with a centralised space to interact with peers around a common theme: E-learning.</p>
    <div class="feature-actions"><a class="btn" href="#">Read more</a><a class="btn btn-signup" href="#">Sign up! Its Free</a></div>
  </article>
  <article class="feature row1">
    <h3 class="feature-title">Discussions</h3>
    <p class="feature-text">Vetrola.club is a Forum and Community Website for Consumers and Providers of MOOCs and Online Learning to meet, share, debate and learn. The site aims to provide its users with a centralised space to interact with peers around a common theme: E-learning.</p>
    <div class="feature-actions"><a class="btn" href="#">Read more</a></div>
  </article>
  <article class="feature row1">
    <h3 class="feature-title">Reviews</h3>
    <p class="feature-text">Vetrola.club is a Forum and Community Website for Consumers and Providers of MOOCs and Online Learning to meet, share, debate and learn. The site aims to provide its users with a centralised space to interact with peers around a common theme: E-learning.</p>
    <div class="feature-actions"><a class="btn" href="#">Read more</a></div>
  </article>
  <article class="feature">
    <h3 class="feature-title">Tips &amp; Guidelines</h3>
    <p class="feature-text">Vetrola.club is a Forum and Community Website for Consumers and Providers of MOOCs and Online Learning to meet, share, debate and learn. The site aims to provide its users with a centralised space to interact with peers around a common theme: E-learning.</p>
    <div class="feature-actions"><a class="btn" href="#">Read more</a></div>
  </article>
  <article class="feature">
    <h3 class="feature-title">News &amp; Articles</h3>
    <p class="feature-text">Vetrola.club is a Forum and Community Website for Consumers and Providers of MOOCs and Online Learning to meet, share, debate and learn. The site aims to provide its users with a centralised space to interact with peers around a common theme: E-learning.</p>
    <div class="feature-actions"><a class="btn" href="#">Read more</a></div>
  </article>
  <article class="feature">
    <h3 class="feature-title">Newsletter</h3>
    <p class="feature-text">Vetrola.club is a Forum and Community Website for Consumers and Providers of MOOCs and Online Learning to meet, share, debate and learn. The site aims to provide its users with a centralised space to interact with peers around a common theme: E-learning.</p>
    <div class="feature-actions"><a class="btn" href="#">Read more</a></div>
  </article>
</section>

<section class="topics">
  <h2 class="topics-title">FREQUENT TOPICS</h2>
  <div class="topics-strip">
    <span class="partner-mark round"></span>
    <span class="partner">Harwick Schools</span>
    <span class="partner">Dunmere</span>
    <span class="partner">Orvalen</span>
    <span class="partner">Kessing College</span>
    <span class="partner">Tarrow State Global</span>
    <span class="partner-mark"></span>
  </div>
</section>

<h2 class="community-title">FROM THE COMMUNITY</h2>
<div class="threads-head">
  <span style="left:187px">RECENT THREADS</span>
  <span style="left:479px">START DATE</span>
  <span style="left:579px">REPLIES</span>
  <span style="left:629px">VIEWS</span>
  <span style="left:692px">LAST MESSAGE</span>
</div>

<ul class="threads">
  <li class="thread tall">
    <span class="avatar photo" role="img" aria-label="Member profile photo"></span>
    <div class="thread-main">
      <div class="thread-title"><span class="tag article">Article</span>Wellcom to Catalix, the new catalan MOOC directory</div>
      <div class="thread-meta">Marcel Oriol, Yesterday at 7:02 PM, Blog</div>
    </div>
    <div class="thread-stats"><div class="stat">Replies: <b>0</b></div><div class="stat">Views: <b>28</b></div></div>
    <div class="last-post"><div class="who">Marcel Oriol</div><div class="when">Yesterday at 7:02 PM</div></div>
  </li>
  <li class="thread">
    <span class="avatar brand-mark">Vetrola</span>
    <div class="thread-main">
      <div class="thread-title"><span class="tag course">Courses</span>Edvanta MOOCs</div>
      <div class="thread-meta">Danica, Yesterday at 9:30 AM, Edvanta</div>
    </div>
    <div class="thread-stats"><div class="stat">Replies: <b>0</b></div><div class="stat">Views: <b>55</b></div></div>
    <div class="last-post"><div class="who">Danica</div><div class="when">Yesterday at 9:30 AM</div></div>
  </li>
  <li class="thread">
    <span class="avatar brand-mark">Vetrola</span>
    <div class="thread-main">
      <div class="thread-title"><span class="tag news">News</span>Vetrola's Learn Scoop promoted to Gold level!</div>
      <div class="thread-meta">Danica, Monday at 6:24 PM, MOOC News</div>
    </div>
    <div class="thread-stats"><div class="stat">Replies: <b>1</b></div><div class="stat">Views: <b>47</b></div></div>
    <div class="last-post"><div class="who">Tomaz</div><div class="when">Tuesday at 2:14 PM</div></div>
  </li>
  <li class="thread">
    <span class="avatar brand-mark">Vetrola</span>
    <div class="thread-main">
      <div class="thread-title"><span class="tag news">News</span>Orrin Academy are looking for a video star!</div>
      <div class="thread-meta">Danica, Tuesday at 8:41 AM, General stuff on course providers</div>
    </div>
    <div class="thread-stats"><div class="stat">Replies: <b>0</b></div><div class="stat">Views: <b>116</b></div></div>
    <div class="last-post"><div class="who">Danica</div><div class="when">Tuesday at 8:41 AM</div></div>
  </li>
  <li class="thread">
    <span class="avatar brand-mark">Vetrola</span>
    <div class="thread-main">
      <div class="thread-title"><span class="tag event">Event</span>What Reviews divulge about Online Education</div>
      <div class="thread-meta">Danica, Monday at 10:52 AM, Events</div>
    </div>
    <div class="thread-stats"><div class="stat">Replies: <b>0</b></div><div class="stat">Views: <b>76</b></div></div>
    <div class="last-post"><div class="who">Danica</div><div class="when">Monday at 10:52 AM</div></div>
  </li>
</ul>

<footer class="site-footer">
  <nav class="footer-nav">
    <a href="#">Home</a><a href="#">Forums</a><a href="#">Resources</a><a href="#">Members</a><a href="#">FAQ</a><a href="#">Blog</a><a href="#">Vetrola Español</a><a href="#">Learn Scoop</a><a href="#">Login</a>
  </nav>
  <div class="footer-social">
    <span class="social-dot"></span><span class="social-dot"></span><span class="social-dot"></span><span class="social-dot"></span>
  </div>
</footer>

</body>
</html>
```